Forget what you know about corporate well

I need a one-page flies used for print, to embedding in a website, all social media platforms and email.

Target Market(s)

Business

Industry/Entity Type

Health And Wellness

Font styles to use
Serif
Script
Other font styles liked:
• I would like the designers opinion on the font

Colors

Designer to choose colors to be used in the design.

Requirements
Must have
• This is the wording:
• Did you know that 75% of healthcare costs are incurred by preventable diseases? Cardiovascular disease, cancer, and diabetes are the three major causes of rising health care plans and are all preventable.
• Owen and his team have spent decades learning how to increase productivity, reduce absenteeism, and increase employee engagement, all leading to lowering healthcare costs. Together, they have developed a system created to target the masses all while addressing individual needs. Their corporate training challenges helps to engrain positive habits through a carefully curated accountability and reward system.
• How it works:
• Step 1 – evaluate the needs of your business;
• Step 2 – set up individualized workshops based on highest needs;
• Step 3 – create a customized corporate training challenge.
• Why Owen?
• Owen excels at motivational speaking. He is an author, a nutritionist and a professional athlete with a master’s degree in clinical nutrition. He is a teacher of corporate wellness at Marbrook College and a health coach. Owen has been featured in national magazines, podcasts, and popular fitness websites. Owen’s own health issues put him on a quest to heal himself and others. With twenty-five years of experience and a passion for wellness, he can provide your company with an unforgettable experience.
Nice to have
• I will not give my opinion, I believe that is an insult to the designer. All of the verbiage is above and I attached a plethora of pictures.
Should not have
• No opinion

```html
<!DOCTYPE html>
<html lang="en">
<head>
<meta charset="utf-8">
<title>Steadfast Wellness – Corporate Wellness Flyer</title>
<link rel="stylesheet" href="https://fonts.googleapis.com/css2?family=Montserrat:wght@600;700;800&family=Questrial&display=swap">
<style>
  :root{
    --charcoal:#26282c;
    --charcoal-deep:#1b1c1f;
    --grey-disc:#9c9d9f;
    --grey-band:#8d8e90;
    --lime:#d3e02a;
    --lime-soft:#c6d42b;
    --green-1:#5aa73a;
    --green-2:#3f9a3f;
    --green-3:#2c8a3d;
    --navy:#141c33;
    --navy-mid:#1f2f5e;
    --blue-glow:#2f4f9a;
    --white:#ffffff;
    --ink:#1d1f22;
  }
  *{box-sizing:border-box;margin:0;padding:0}
  html,body{width:707px;height:1200px;overflow:hidden;background:var(--charcoal-deep)}
  .flyer{
    position:relative;width:707px;height:1200px;overflow:hidden;
    background:linear-gradient(180deg,var(--charcoal) 0%,#2e3035 50%,#23252a 100%);
    font-family:"Questrial",sans-serif;color:var(--white);
  }
  .hero-art{position:absolute;left:0;top:0;width:707px;height:764px}
  .brand{position:absolute;left:30px;top:42px;width:230px;text-align:center}
  .brand-mark{width:32px;height:32px;border-radius:50%;background:var(--white);margin:0 auto 10px}
  .brand-name{font-size:18px;color:var(--white);letter-spacing:.3px}
  .headline-block{position:absolute;left:0;top:610px;width:707px;text-align:center}
  .headline{
    font-family:"Montserrat",sans-serif;font-weight:800;font-size:40px;
    color:var(--lime);letter-spacing:.3px;line-height:1.05;
  }
  .subhead{
    font-family:"Montserrat",sans-serif;font-weight:600;font-size:17.5px;
    color:var(--white);letter-spacing:.1px;margin-top:6px;
  }
  .lede{font-size:14.5px;line-height:1.38;margin:10px auto 0;width:540px}
  .mission{
    position:absolute;left:0;top:764px;width:707px;height:116px;background:var(--grey-band);
    display:flex;align-items:center;justify-content:center;
  }
  .mission p{width:620px;text-align:center;font-size:11.6px;line-height:1.5}
  .steps{position:absolute;left:0;top:880px;width:707px;height:66px}
  .steps-bg{position:absolute;inset:0;width:707px;height:66px}
  .step{position:absolute;top:0;height:66px;display:flex;align-items:center;gap:12px}
  .step-num{
    width:32px;height:32px;border-radius:50%;background:var(--white);color:var(--ink);
    border:2px solid #d9d9d9;display:flex;align-items:center;justify-content:center;
    font-family:"Montserrat",sans-serif;font-weight:600;font-size:17px;flex:none;
  }
  .step-text{font-size:11.5px;line-height:1.25}
  .why{
    position:absolute;left:0;top:946px;width:707px;height:202px;
    background:radial-gradient(ellipse at 70% 20%,var(--navy-mid) 0%,var(--navy) 70%);
    text-align:center;
  }
  .why h2{font-family:"Montserrat",sans-serif;font-weight:700;font-size:22px;margin-top:22px}
  .why-rule{width:120px;height:2px;background:var(--lime);margin:6px auto 14px}
  .why p{width:640px;margin:0 auto;font-size:11.5px;line-height:1.5}
  .footer{position:absolute;left:0;top:1148px;width:707px;height:52px}
  .footer-bg{position:absolute;inset:0;width:707px;height:52px}
  .site{position:absolute;left:28px;top:0;height:52px;display:flex;align-items:center;gap:16px;font-size:18px}
  .globe{width:26px;height:26px;flex:none}
  .cta{
    position:absolute;right:18px;top:0;height:52px;display:flex;align-items:center;gap:6px;
    color:var(--ink);font-family:"Montserrat",sans-serif;
  }
  .cta-lead{font-size:17px;font-weight:600}
  .cta-call{font-size:14px;font-weight:800}
  .cta-phone{font-size:24px;font-weight:800;letter-spacing:-.3px}
</style>
</head>
<body>
<main class="flyer">
  <svg class="hero-art" viewBox="0 0 707 764">
    <defs>
      <linearGradient id="eventTone" x1="0" y1="0" x2="1" y2="1">
        <stop offset="0" stop-color="#3a3c42"/>
        <stop offset=".45" stop-color="#5a5550"/>
        <stop offset=".75" stop-color="#6a3636"/>
        <stop offset="1" stop-color="#2a2c31"/>
      </linearGradient>
      <linearGradient id="portraitTone" x1="0" y1="0" x2="0" y2="1">
        <stop offset="0" stop-color="#cfd6d8"/>
        <stop offset=".55" stop-color="#b58f7c"/>
        <stop offset="1" stop-color="#8a2a2e"/>
      </linearGradient>
      <radialGradient id="blueSweep" cx=".1" cy="1" r="1">
        <stop offset="0" stop-color="var(--blue-glow)" stop-opacity=".85"/>
        <stop offset="1" stop-color="var(--blue-glow)" stop-opacity="0"/>
      </radialGradient>
    </defs>
    <rect x="0" y="480" width="707" height="284" fill="url(#blueSweep)"/>
    <path role="img" aria-label="Photo of the speaker presenting a workshop to a group seated among exercise bikes"
          d="M290 0 H707 V560 C610 590 480 585 410 525 C340 465 305 370 330 260 C350 170 325 80 290 0 Z"
          fill="url(#eventTone)"/>
    <circle cx="125" cy="25" r="172" fill="var(--grey-disc)"/>
    <circle cx="395" cy="215" r="335" fill="none" stroke="var(--white)" stroke-width="1.2" opacity=".8"/>
    <circle cx="197" cy="355" r="126" fill="none" stroke="var(--lime)" stroke-width="2"/>
    <circle cx="197" cy="355" r="110" fill="var(--white)"/>
    <circle role="img" aria-label="Portrait of the wellness coach" cx="197" cy="355" r="104" fill="url(#portraitTone)"/>
    <circle cx="226" cy="212" r="18" fill="var(--lime)"/>
  </svg>

  <div class="brand">
    <div class="brand-mark"></div>
    <div class="brand-name">Steadfast Wellness</div>
  </div>

  <section class="headline-block">
    <h1 class="headline">DID YOU KNOW THAT 75% OF</h1>
    <p class="subhead">HEALTHCARE COSTS ARE INCURRED BY PREVENTABLE DISEASES?</p>
    <p class="lede">Cardiovascular disease, cancer, and diabetes are the three major causes of rising health care plans and are all preventable.</p>
  </section>

  <section class="mission">
    <p>Owen and his team have spent decades learning how to increase productivity, reduce absenteeism, and increase employee engagement, all leading to lowering healthcare costs. Together, they have developed a system created to target the masses all while addressing individual needs. Their corporate training challenges helps to engrain positive habits through a carefully curated accountability and reward system.</p>
  </section>

  <section class="steps">
    <svg class="steps-bg" viewBox="0 0 707 66" preserveAspectRatio="none" aria-hidden="true">
      <polygon points="0,0 232,0 252,33 232,66 0,66" fill="var(--green-1)"/>
      <polygon points="232,0 478,0 498,33 478,66 232,66 252,33" fill="var(--green-2)"/>
      <polygon points="478,0 707,0 707,66 478,66 498,33" fill="var(--green-3)"/>
    </svg>
    <div class="step" style="left:24px"><span class="step-num">1</span><span class="step-text">Evaluate the needs of<br>your business;</span></div>
    <div class="step" style="left:264px"><span class="step-num">2</span><span class="step-text">Set up individualized workshops<br>based on highest needs;</span></div>
    <div class="step" style="left:510px"><span class="step-num">3</span><span class="step-text">Create a customized<br>corporate training challenge.</span></div>
  </section>

  <section class="why">
    <h2>Why Owen?</h2>
    <div class="why-rule"></div>
    <p>Owen excels at motivational speaking. He is an author, a nutritionist and a professional athlete with a master’s degree in clinical nutrition. He is a teacher of corporate wellness at Marbrook College and a health coach. Owen has been featured in national magazines, podcasts, and popular fitness websites. Owen’s own health issues put him on a quest to heal himself and others. With twenty-five years of experience and a passion for wellness, he can provide your company with an unforgettable experience.</p>
  </section>

  <footer class="footer">
    <svg class="footer-bg" viewBox="0 0 707 52" preserveAspectRatio="none" aria-hidden="true">
      <rect x="0" y="0" width="707" height="52" fill="var(--grey-band)"/>
      <polygon points="300,0 707,0 707,52 328,52" fill="var(--lime-soft)"/>
    </svg>
    <div class="site">
      <svg class="globe" viewBox="0 0 26 26" aria-hidden="true">
        <circle cx="13" cy="13" r="12" fill="var(--lime)"/>
        <circle cx="13" cy="13" r="7.5" fill="none" stroke="var(--ink)" stroke-width="1.2"/>
        <ellipse cx="13" cy="13" rx="3.4" ry="7.5" fill="none" stroke="var(--ink)" stroke-width="1.1"/>
        <line x1="5.5" y1="13" x2="20.5" y2="13" stroke="var(--ink)" stroke-width="1.1"/>
      </svg>
      <span>www.owenmarlow.com</span>
    </div>
    <div class="cta">
      <span class="cta-lead">GET STARTED!</span>
      <span class="cta-call">CALL</span>
      <span class="cta-phone">(555) 014-0237</span>
    </div>
  </footer>
</main>
</body>
</html>
```